Blog design for health, nutrition and exercise blogging (fernquillhub.com)

FernquillHub.com will be run by an exercise and nutritional scientist and aims to provide educational evidence-based articles on a variety of topics related to nutrition, exercise, sports, nutritional supplements and health.

The articles will cover topics like:
• Translating science into layman’s terms
• Age-specific nutritional advice
• Interpreting food and supplement labels properly
• Demystifying nutritional supplements
• Supplements and nutrition for sports and exercise performance

Target Market(s)

The target audience is the mainstream public across all age groups and is not necessarily restricted to sports persons.

Industry/Entity Type

Health And Wellness

Coding

Coded - Design and coding required

Number of Pages Required

5+ page

Font styles to use
Sans Serif

Requirements
Must have
• • About FernquillHub.com and its mission
• • About author-highlighting background, publications and achievements
• • Easily accessible website sections
• • Easy article categorization (see below)
• • Clear navigation
• • Easy to manage website (frequent article/ blog updates)
• • Easy links to social media pages (Facebook/ twitter/ etc.)
• • Easy to share articles
• • Mobile and tablet friendly
• • Contact and feedback submission form
• • Community section to build a forum and following
• Article categorization
• The following tabs need to be present to categorize the articles
• A. Nutrition, with the subsections below:
• Proteins/ amino acids
• Carbohydrates
• Fats
• Herbals and Nutraceuticals
• Vitamins and minerals
• B. Exercise and Sports
• C. Age-specific: children, teen, adults, seniors (may contain articles from other categories)
• D. Condition-specific: e.g. obesity, ageing, diabetes, Alzheimer’s, etc. (may contain articles from other categories)
• Website logo-depicting science and health/ fitness
• Health/ Fitness/ Lifestyle/ Science (DNA strands, etc.)/
• Bodybuilding Images
• images of active and exercising kids, young adults and elderly
• Images of herbs to depict preference for natural alternatives with regard to nutrition and supplementation
• Images of supplement containers-protein powders/ capsules/ gel capsules etc.

```html
<!DOCTYPE html>
<html lang="en">
<head>
<meta charset="utf-8">
<title>FernquillHub – Think About Yourself</title>
<link rel="stylesheet" href="https://fonts.googleapis.com/css2?family=Open+Sans:wght@400;600;700;800&display=swap">
<style>
  :root {
    --page-bg: #e9e6e1;
    --screen-bg: #ffffff;
    --header-bg: #3b3d3f;
    --brand-green: #4fc879;
    --icon-grey: #c9cbcd;
    --hero-red: #b3261e;
    --hero-green: #4f8a2c;
    --hero-purple: #5b2a5c;
    --hero-orange: #e2822b;
    --card-border: #e3e3e3;
    --title-ink: #2b2b2b;
    --body-ink: #6d6d6d;
    --white: #ffffff;
  }
  * { box-sizing: border-box; margin: 0; padding: 0; }
  html, body {
    width: 1200px; height: 800px; overflow: hidden;
    background: var(--page-bg);
    font-family: "Open Sans", Arial, sans-serif;
  }
  .canvas {
    width: 1200px; height: 800px;
    display: flex; align-items: center; justify-content: center;
  }
  .mobile-page {
    width: 540px; height: 740px;
    background: var(--screen-bg);
    overflow: hidden;
    display: flex; flex-direction: column;
    box-shadow: 0 6px 24px rgba(0,0,0,0.12);
  }
  .site-header {
    height: 52px; flex: none;
    background: var(--header-bg);
    display: flex; align-items: stretch; justify-content: space-between;
    padding: 0 18px;
  }
  .menu-toggle, .search-toggle {
    display: flex; align-items: center; width: 36px;
  }
  .search-toggle { justify-content: flex-end; }
  .brand {
    background: var(--brand-green);
    color: var(--white);
    font-weight: 700;
    font-size: 26px;
    letter-spacing: -0.3px;
    display: flex; align-items: center;
    padding: 0 26px;
    margin-top: 6px;
  }
  .hero {
    position: relative; height: 340px; flex: none;
  }
  .hero-photo {
    position: absolute; inset: 0;
    background:
      radial-gradient(circle at 22% 78%, var(--hero-purple) 0 16%, transparent 30%),
      radial-gradient(circle at 70% 45%, var(--hero-purple) 0 10%, transparent 22%),
      radial-gradient(circle at 40% 20%, var(--hero-red) 0 12%, transparent 26%),
      radial-gradient(circle at 45% 65%, var(--hero-orange) 0 10%, transparent 24%),
      radial-gradient(circle at 85% 40%, #e4c23a 0 8%, transparent 20%),
      linear-gradient(135deg, var(--hero-green), #3f7a2a 50%, var(--hero-green));
  }
  .hero-title {
    position: absolute; left: 22px; top: 70px;
    color: var(--white);
    font-weight: 800;
    font-size: 38px;
    letter-spacing: -0.5px;
    text-shadow: 0 2px 6px rgba(0,0,0,0.45);
  }
  .post-list {
    flex: 1;
    display: grid; grid-template-columns: 1fr 1fr; gap: 18px;
    padding: 22px 22px 0;
  }
  .post-card {
    border: 1px solid var(--card-border);
    padding: 8px 8px 14px;
  }
  .post-photo {
    height: 130px;
    background:
      radial-gradient(circle at 30% 30%, var(--hero-red) 0 14%, transparent 28%),
      radial-gradient(circle at 70% 60%, var(--hero-purple) 0 12%, transparent 26%),
      radial-gradient(circle at 45% 75%, var(--hero-orange) 0 10%, transparent 22%),
      linear-gradient(135deg, var(--hero-green), #3f7a2a);
  }
  .post-title {
    font-size: 12px; font-weight: 700; color: var(--title-ink);
    margin: 14px 4px 10px;
  }
  .post-excerpt {
    font-size: 10px; line-height: 1.55; color: var(--body-ink);
    margin: 0 4px;
  }
</style>
</head>
<body>
<div class="canvas">
  <main class="mobile-page">
    <header class="site-header">
      <div class="menu-toggle" aria-label="Menu">
        <svg width="26" height="18" viewBox="0 0 26 18"><g stroke="var(--icon-grey)" stroke-width="2"><line x1="0" y1="2" x2="26" y2="2"/><line x1="0" y1="9" x2="26" y2="9"/><line x1="0" y1="16" x2="26" y2="16"/></g></svg>
      </div>
      <div class="brand">fernquillhub</div>
      <div class="search-toggle" aria-label="Search">
        <svg width="20" height="20" viewBox="0 0 20 20"><g stroke="var(--icon-grey)" stroke-width="2" fill="none"><circle cx="11" cy="8" r="6"/><line x1="7" y1="12.5" x2="1.5" y2="18"/></g></svg>
      </div>
    </header>
    <section class="hero">
      <div class="hero-photo" role="img" aria-label="Photo of fresh vegetables: tomatoes, carrots, aubergine, peppers, cabbage and greens"></div>
      <h1 class="hero-title">THINK ABOUT YOURSELF</h1>
    </section>
    <section class="post-list">
      <article class="post-card">
        <div class="post-photo" role="img" aria-label="Photo of assorted fresh vegetables"></div>
        <h2 class="post-title">This is blog post title</h2>
        <p class="post-excerpt">Fresh seasonal vegetables supply fibre, vitamins and minerals that support steady energy. Learn how simple swaps at each meal can improve your daily nutrition and help your body recover after regular exercise.</p>
      </article>
      <article class="post-card">
        <div class="post-photo" role="img" aria-label="Photo of assorted fresh vegetables"></div>
        <h2 class="post-title">This is blog post title</h2>
        <p class="post-excerpt">Protein, carbohydrates and healthy fats each play a distinct role in training. This short guide explains what the research says and how to read food labels before choosing any supplement for your routine.</p>
      </article>
    </section>
  </main>
</div>
</body>
</html>
```